Business Card Design

Im a small business that specialises in all aspects of sign installation, big and small, domestic and commercial. I have a construction and carpentry background. I'm after a professional looking business card, that has my logo as the forefront of the card incorporating the same colours as the my logo. No slogan as yet, but open to suggestions. The final design should communicate quality and class workmanship.

Target Market(s)

Managers and Owners of businesses

Industry/Entity Type

Small Business

Contact Information for Business Card

Carwyn Solbeck
Mob: 0417295036
Email: kto.fitouts@quillmail.net

Sign Installation
Property Improvement and Maintenance
Trade Services

Colors
dbdbdb
000000
ffffff

Requirements
Must have
• Logo
My name
My contact details
What I specialise in
Nice to have
• background image/images that are only just noticeable and do not take away from the logo or text.
Should not have
• No colours that contrast from my logo
No heavy machinery images to be used
Logo must stand out

```html
<!DOCTYPE html>
<html lang="en">
<head>
<meta charset="utf-8">
<title>Kavell Installations – Business Card</title>
<link rel="stylesheet" href="https://fonts.googleapis.com/css2?family=Open+Sans:wght@400;600;700&display=swap">
<style>
  :root {
    --brand-blue: #1b4f9c;
    --ink: #1e1e1e;
    --muted: #555555;
    --paper: #ffffff;
    --paper-shade: #f1f1f1;
    --stage: #dbdbdb;
  }
  * { box-sizing: border-box; margin: 0; padding: 0; }
  html, body {
    width: 1200px; height: 1012px; overflow: hidden;
    background: var(--stage);
    font-family: "Open Sans", Arial, sans-serif;
    color: var(--ink);
  }
  .sheet {
    width: 1200px; height: 1012px;
    display: flex; flex-direction: column;
    align-items: center; justify-content: center; gap: 56px;
  }
  .card {
    position: relative;
    width: 720px; height: 411px;
    background: linear-gradient(135deg, var(--paper) 55%, var(--paper-shade));
    box-shadow: 0 10px 28px rgba(0,0,0,.18);
    overflow: hidden;
  }
  /* Front */
  .card--front { border-bottom: 6px solid var(--brand-blue); }
  .card__texture {
    position: absolute; right: 0; top: 60px;
    width: 430px; height: 260px;
    background: radial-gradient(ellipse at 40% 60%, rgba(27,79,156,.07), rgba(27,79,156,0) 70%);
  }
  .brand {
    position: absolute;
    display: flex; align-items: center; gap: 14px;
  }
  .brand__dot {
    width: 46px; height: 46px; border-radius: 50%;
    background: var(--brand-blue); flex: none;
  }
  .brand__name {
    font-weight: 700; color: var(--brand-blue);
    letter-spacing: .04em; line-height: 1.05;
    text-transform: uppercase;
  }
  .card--front .brand { left: 52px; top: 168px; }
  .card--front .brand__name { font-size: 30px; }
  .contact {
    position: absolute; left: 400px; top: 128px;
  }
  .contact__name { font-size: 21px; font-weight: 400; }
  .contact__role { font-size: 16px; font-weight: 700; color: var(--brand-blue); margin-top: 2px; }
  .contact__list { list-style: none; margin-top: 22px; }
  .contact__item {
    display: flex; align-items: center; gap: 12px;
    font-size: 16px; margin-bottom: 12px;
  }
  .contact__icon { width: 18px; height: 18px; fill: var(--brand-blue); flex: none; }
  /* Back */
  .card--back .brand {
    left: 50%; top: 120px; transform: translateX(-50%);
    flex-direction: column; gap: 16px;
  }
  .card--back .brand__dot { width: 60px; height: 60px; }
  .card--back .brand__name { font-size: 40px; text-align: center; }
  .services {
    position: absolute; left: 0; right: 0; top: 300px;
    text-align: center; font-size: 17px; color: var(--muted);
  }
  .services__sep { margin: 0 10px; color: #999; }
</style>
</head>
<body>
<main class="sheet">
  <section class="card card--front" aria-label="Card front">
    <div class="card__texture"></div>
    <div class="brand">
      <span class="brand__dot"></span>
      <span class="brand__name">Kavell<br>Installations</span>
    </div>
    <div class="contact">
      <p class="contact__name">Carwyn Solbeck Mob</p>
      <p class="contact__role">Managing Director</p>
      <ul class="contact__list">
        <li class="contact__item">
          <svg class="contact__icon" viewBox="0 0 24 24"><path d="M6.6 10.8a15.1 15.1 0 0 0 6.6 6.6l2.2-2.2a1 1 0 0 1 1-.25 11.4 11.4 0 0 0 3.6.57 1 1 0 0 1 1 1V20a1 1 0 0 1-1 1A17 17 0 0 1 3 4a1 1 0 0 1 1-1h3.5a1 1 0 0 1 1 1c0 1.25.2 2.45.57 3.57a1 1 0 0 1-.25 1z"/></svg>
          <span>0417295036</span>
        </li>
        <li class="contact__item">
          <svg class="contact__icon" viewBox="0 0 24 24"><path d="M2 5h20v14H2z" fill="none"/><path d="M2 5h20v14H2V5zm2 2v.4l8 5.1 8-5.1V7H4z"/></svg>
          <span>kto.fitouts@quillmail.net</span>
        </li>
      </ul>
    </div>
  </section>

  <section class="card card--back" aria-label="Card back">
    <div class="brand">
      <span class="brand__dot"></span>
      <span class="brand__name">Kavell Installations</span>
    </div>
    <p class="services">
      Sign Installation<span class="services__sep">|</span>Property improvement and maintenance<span class="services__sep">|</span>Trade Services
    </p>
  </section>
</main>
</body>
</html>
```